Software company WebSite Design (enterprise level SW, Mobile apps, HW prototypes)

We need design for our new webpages. We got new logo and new business cards and we need webdesign which will be match with those two.
We are dealing with corporate level software development - enterprise level portals, development of optimalization SW, route planning optimalizations. For a few months we are developing mobile applications for companies.
IMPORTANT is to express the cutting edge technological company.

Target Market(s)

IT company customers

Industry/Entity Type

Business

Number of Pages Required

2 page

Requirements
Must have
• Project needs to have landing page and product detail page. Design needs to be created including full font and example images as there would be a real webpage. Design should be clean, modern and expressing hi-tech level of the company.
• Example of well designer web pages - www.quolvent.com, www.brandovi.com - We like the font formatting and font designs (colors, placing, etc - its professional).
• Attached image contains screenshot from old web landing page. It contains basic sections of our business (Simulation Tools, Enterprise Intranet Systems, Hi-tech web presentations, Supporting Enterprise services - Optimalization and logistics monitoring)

```html
<!DOCTYPE html>
<html lang="en">
<head>
<meta charset="utf-8">
<title>Velorix Solutions</title>
<link rel="stylesheet" href="https://fonts.googleapis.com/css2?family=Open+Sans:wght@400;600;700&display=swap">
<style>
:root{
  --red:#d0121b;
  --blue:#1a82c9;
  --sky:#3db4f0;
  --orange:#ff7425;
  --rust:#d8470e;
  --ink:#2b2b2b;
  --text:#555;
  --muted:#888;
  --line:#e3e3e3;
  --footer:#2a2a2a;
  --grey-bg:#f2f2f2;
}
*{box-sizing:border-box;margin:0;padding:0}
html,body{width:1200px;height:2174px;overflow:hidden}
body{position:relative;font-family:"Open Sans",Arial,sans-serif;color:var(--text);background:#fff}
.abs{position:absolute}
a{color:inherit;text-decoration:none}

/* header */
.topline{left:0;top:0;width:1200px;height:3px;background:var(--red)}
.header{left:0;top:3px;width:1200px;height:98px;background:#fff}
.brand{display:flex;align-items:center;gap:12px}
.brand-mark{width:34px;height:34px;background:var(--red)}
.brand-name{font-weight:700;font-size:22px;color:var(--ink);letter-spacing:.3px;white-space:nowrap}
.header .brand{left:160px;top:32px}
.call{left:708px;top:22px;font-size:11px;color:var(--ink);display:flex;align-items:center;gap:6px}
.call b{color:var(--red);font-weight:400}
.search{left:890px;top:17px;width:149px;height:25px;border:1px solid var(--line);border-radius:3px;font-size:10px;color:var(--muted);font-style:italic;padding:5px 0 0 24px}
.search svg{position:absolute;left:8px;top:7px}
.nav a{position:absolute;top:58px;height:26px;line-height:26px;font-size:10.5px;font-weight:700;color:var(--ink);white-space:nowrap}
.nav a.active{background:var(--blue);color:#fff;width:59px;text-align:center}

/* hero */
.hero{left:0;top:101px;width:1200px;height:506px;background:linear-gradient(90deg,#dfe8ef 0%,#c9d6e2 35%,#4f6486 62%,#1f2d4a 85%,#2c3b5b 100%)}
.hero-title{left:161px;top:255px;font-size:32px;font-weight:700;color:var(--ink)}
.hero-title span,.hl{color:var(--red)}
.hero-text{left:161px;top:311px;width:375px;font-size:12.3px;line-height:19px;color:#444}
.btn{height:41px;line-height:41px;font-size:12px;font-weight:700;color:#fff;border-radius:2px;text-align:center}
.btn-join{left:162px;top:394px;width:99px;background:var(--blue)}
.btn-more{left:274px;top:394px;width:100px;background:var(--red)}
.hero-arrow{width:34px;height:34px;border:2px solid rgba(255,255,255,.85);border-radius:50%;display:flex;align-items:center;justify-content:center}

/* section heads */
.sec-head{left:0;width:1200px;display:flex;justify-content:center;align-items:center;gap:8px;font-size:23px;font-weight:700;color:var(--ink)}
.sec-head i{display:block;width:16px;height:16px;background:var(--red)}
.sec-head.light{color:#fff}
.sec-head.light i{background:#fff}
.intro{left:240px;top:682px;width:720px;text-align:center;font-size:11px;line-height:19px;color:#444}

/* feature cards */
.feature{top:782px;width:272px;height:203px;border:1px solid var(--line);text-align:center;background:#fff}
.feature h3{margin-top:64px;font-size:15px;font-weight:600;line-height:17px;color:var(--ink)}
.feature p{margin:16px auto 0;width:240px;font-size:11px;line-height:19px}
.read{display:block;margin-top:10px;font-size:10px;font-weight:700;color:var(--red)}
.hexicon{top:730px;width:88px;height:88px}

/* business band */
.band{left:0;top:1026px;width:1200px;height:406px;background:linear-gradient(180deg,#3fb6f1,#35aeea)}
.notch{left:584px;top:1026px;width:0;height:0;border-left:16px solid transparent;border-right:16px solid transparent;border-top:14px solid #fff}
.biz{top:1124px;width:206px;height:264px;background:#fff;text-align:center}
.biz .ph{height:111px}
.biz h3{margin-top:16px;font-size:14.5px;font-weight:600;line-height:17px;color:var(--ink)}
.biz p{margin:12px auto 0;width:184px;font-size:11px;line-height:18px}
.biz .bar{position:absolute;left:0;bottom:0;width:100%;height:32px;line-height:32px;font-size:10.5px;font-weight:700;color:#fff}

/* about */
.col-head{font-size:23px;font-weight:700;color:var(--ink);display:flex;align-items:center;gap:8px}
.col-head i{display:block;width:16px;height:16px;background:var(--red)}
.pic{border:3px solid #fff;box-shadow:0 0 0 1px #cfcfcf}
.about-text{width:200px;font-size:11px;line-height:18.5px;color:#444}
.about-text p+p{margin-top:8px}
.about-text .read{margin-top:8px}
.divider{left:0;top:1729px;width:1200px;height:2px;background:#e8e8e8}

/* customers */
.customers{left:0;top:1731px;width:1200px;height:173px;background:var(--grey-bg)}
.logos{left:160px;top:1838px;width:880px;display:flex;justify-content:space-between;align-items:center;font-size:20px;font-weight:600;color:#7d7d7d}
.logos span{display:flex;align-items:center;gap:7px}
.logos i{display:block;width:20px;height:20px;border-radius:50%;background:#8a8a8a}
.logos i.sq{border-radius:0}

/* footer */
.footer{left:0;top:1904px;width:1200px;height:216px;background:var(--footer);color:#c9c9c9}
.foot-brand .brand-name{color:#fff}
.foot-about{left:160px;top:2013px;width:185px;font-size:10.5px;line-height:18px;color:#d0d0d0}
.fcol{top:1943px;font-size:10.5px}
.fcol h4{font-size:12px;font-weight:700;color:#fff;margin-bottom:14px}
.fcol li{list-style:none;line-height:20.3px;color:#cfcfcf}
.fcol li:before{content:"›";margin-right:8px;color:#fff}
.where p{display:flex;gap:10px;font-size:10.5px;line-height:17px;color:#cfcfcf;margin-bottom:14px}
.where .tel{color:var(--red);font-size:12.5px}
.bottom{left:0;top:2120px;width:1200px;height:54px;background:var(--red);color:#fff;font-size:10.5px}
.copy{left:161px;top:19px}
.socials{left:921px;top:13px;display:flex;gap:5px}
.socials span{width:27px;height:27px;border:1.5px solid #fff;border-radius:50%}
.code{left:1098px;top:17px;font-size:9px}
</style>
</head>
<body>

<div class="abs topline"></div>
<header class="abs header">
  <div class="abs brand"><span class="brand-mark"></span><span class="brand-name">Velorix Solutions</span></div>
  <div class="abs call">
    <svg width="10" height="10" viewBox="0 0 10 10"><path d="M2 0h3l1 3-1.5 1a6 6 0 0 0 2 2L7.5 4.5 10 5.5V8a2 2 0 0 1-2 2A8 8 0 0 1 0 2 2 2 0 0 1 2 0z" fill="#333"/></svg>
    CALL US ON: <b>+420 555 010 482</b>
  </div>
  <div class="abs search"><svg width="9" height="9" viewBox="0 0 10 10"><circle cx="4" cy="4" r="3" fill="none" stroke="#333" stroke-width="1.4"/><path d="M6.5 6.5 9.5 9.5" stroke="#333" stroke-width="1.4"/></svg>Search</div>
  <nav class="nav">
    <a class="active" href="#" style="left:481px">HOME</a>
    <a href="#" style="left:572px">ABOUT US</a>
    <a href="#" style="left:671px">SERVICES</a>
    <a href="#" style="left:768px">PRICING</a>
    <a href="#" style="left:860px">DEVELOPERS</a>
    <a href="#" style="left:972px">CONTACT US</a>
  </nav>
</header>

<section>
  <div class="abs hero" role="img" aria-label="Photo of two businessmen in suits reviewing work together in a bright office"></div>
  <h1 class="abs hero-title">VELORIX <span>SOLUTIONS</span></h1>
  <p class="abs hero-text">Sed ut perspiciatis unde omnis iste natus error sit voluptatem accu santium doloremque laudantium, totam rem aperiam, eaque ipsa quae ab illo inventore veritatis et qu</p>
  <a class="abs btn btn-join" href="#">JOIN US</a>
  <a class="abs btn btn-more" href="#">READ MORE</a>
  <div class="abs hero-arrow" style="left:36px;top:322px"><svg width="10" height="12" viewBox="0 0 10 12"><path d="M7 1 2 6l5 5" fill="none" stroke="#fff" stroke-width="1.8"/></svg></div>
  <div class="abs hero-arrow" style="left:1126px;top:322px"><svg width="10" height="12" viewBox="0 0 10 12"><path d="M3 1l5 5-5 5" fill="none" stroke="#fff" stroke-width="1.8"/></svg></div>
</section>

<section>
  <h2 class="abs sec-head" style="top:632px"><i></i>WE ARE A SOFTWARE <span class="hl">DEVELOPMENT COMPANY</span></h2>
  <p class="abs intro">Sed ut perspiciatis unde omnis iste natus error sit voluptatem accusantium doloremque laudantium, totam rem aperiam, eaque ipsa quae ab illo inventore veritatis et quasi architecto beatae vitae dicta sunt explicaboemo enim ipsam voluptatem quia voluptas sit asper.</p>

  <article class="abs feature" style="left:160px"><h3>Enterprise<br>Level Portals</h3><p>Sed ut perspiciatis unde omnis isnatus error sitatem accolosa ntium doloremque mined ut perspiciatis unde omnis isnatus lorem.</p><a class="read" href="#">READ MORE</a></article>
  <article class="abs feature" style="left:464px"><h3>Development of<br>optimalization SW</h3><p>Sed ut perspiciatis unde omnis isnatus error sitatem accolosa ntium doloremque mined ut perspiciatis unde omnis isnatus lorem.</p><a class="read" href="#">READ MORE</a></article>
  <article class="abs feature" style="left:765px"><h3>Route planning<br>Optimalizations</h3><p>Sed ut perspiciatis unde omnis isnatus error sitatem accolosa ntium doloremque mined ut perspiciatis unde omnis isnatus lorem.</p><a class="read" href="#">READ MORE</a></article>

  <svg class="abs hexicon" style="left:253px" viewBox="0 0 88 88"><path d="M30 2h28l28 28v28L58 86H30L2 58V30z" fill="var(--orange)"/><g fill="#fff"><circle cx="44" cy="36" r="6"/><circle cx="32" cy="39" r="4.5"/><circle cx="56" cy="39" r="4.5"/><path d="M34 56a10 10 0 0 1 20 0z"/><path d="M24 54a8 8 0 0 1 12-5l-2 5z"/><path d="M64 54a8 8 0 0 0-12-5l2 5z"/></g></svg>
  <svg class="abs hexicon" style="left:556px" viewBox="0 0 88 88"><path d="M30 2h28l28 28v28L58 86H30L2 58V30z" fill="var(--sky)"/><g fill="none" stroke="#fff" stroke-width="4"><circle cx="40" cy="46" r="7"/><circle cx="54" cy="34" r="4"/></g><g stroke="#fff" stroke-width="3"><path d="M40 34v4M40 54v4M28 46h4M48 46h4M32 38l3 3M45 51l3 3M32 54l3-3M45 41l3-3"/></g></svg>
  <svg class="abs hexicon" style="left:857px" viewBox="0 0 88 88"><path d="M30 2h28l28 28v28L58 86H30L2 58V30z" fill="var(--red)"/><path d="M60 28 28 42l10 4 4 12 6-8 8 4z" fill="#fff"/><path d="M38 46l22-18-16 22z" fill="#f2c9cb"/></svg>
</section>

<section>
  <div class="abs band"></div>
  <div class="abs notch"></div>
  <h2 class="abs sec-head light" style="top:1064px"><i></i>IT CONTAINS BASIC SECTIONS OF OUR BUSINESS</h2>

  <article class="abs biz" style="left:160px"><div class="ph" role="img" aria-label="Photo of hands working with charts on a tablet" style="background:linear-gradient(135deg,#e8eef4,#9fb3c8)"></div><h3>Simulation Tools</h3><p>Sed ut perspiciatis unde omnistus sitatem accolosa ntium doloSedut perspiciatis unde omnist.</p><a class="bar" href="#" style="background:var(--red)">READ MORE</a></article>
  <article class="abs biz" style="left:384px"><div class="ph" role="img" aria-label="Illustration of a hand with glowing network technology" style="background:linear-gradient(135deg,#0e2a3a,#2f6f86)"></div><h3>Enterprise<br>Intranet Systems</h3><p>Sed ut perspiciatis unde omnistus sitatem accolosa ntium dolo.</p><a class="bar" href="#" style="background:var(--orange)">READ MORE</a></article>
  <article class="abs biz" style="left:607px"><div class="ph" role="img" aria-label="Photo of an audience at a conference presentation" style="background:linear-gradient(135deg,#2a3348,#8a4a3a)"></div><h3>Hi-tech web<br>Presentations</h3><p>Sed ut perspiciatis unde omnistus sitatem accolosa ntium dolo.</p><a class="bar" href="#" style="background:var(--blue)">READ MORE</a></article>
  <article class="abs biz" style="left:832px"><div class="ph" role="img" aria-label="Photo of a support team working at computers" style="background:linear-gradient(135deg,#4a4f55,#b0a89c)"></div><h3>Supporting<br>Enterprise services</h3><p>Sed ut perspiciatis unde omnistus sitatem accolosa ntium dolo.</p><a class="bar" href="#" style="background:var(--rust)">READ MORE</a></article>
</section>

<section>
  <h2 class="abs col-head" style="left:160px;top:1465px"><i></i>WHO <span class="hl">WE ARE</span></h2>
  <div class="abs pic" role="img" aria-label="Photo of a business team meeting around a table" style="left:160px;top:1521px;width:206px;height:160px;background:linear-gradient(135deg,#d9d4cc,#8d7f70)"></div>
  <div class="abs about-text" style="left:385px;top:1516px">
    <p>Sed ut perspiciatis unde omnis iste natus error sit voluptatem accusant ium doloremque laudantium, totam rem aperiam, eaque ipsa.</p>
    <p>Auae ab illo inventore veritatis et quasi architecto beatae vitae dicta sunt expli cabomo enim ipsam voluptatem.</p>
    <a class="read" href="#">READ MORE</a>
  </div>

  <h2 class="abs col-head" style="left:627px;top:1465px"><i></i>OUR SUPPORT IS <span class="hl">LEGENDARY</span></h2>
  <div class="abs pic" role="img" aria-label="Photo of two colleagues working together at a laptop" style="left:624px;top:1521px;width:206px;height:160px;background:linear-gradient(135deg,#eef3f6,#6f9cc0)"></div>
  <div class="abs about-text" style="left:849px;top:1516px">
    <p>Sed ut perspiciatis unde omnis iste natus error sit voluptatem accusant ium doloremque laudantium, totam rem aperiam, eaque ipsa.</p>
    <p>Auae ab illo inventore veritatis et quasi architecto beatae vitae dicta sunt expli cabomo enim ipsam voluptatem.</p>
    <a class="read" href="#">READ MORE</a>
  </div>
  <div class="abs divider"></div>
</section>

<section>
  <div class="abs customers"></div>
  <h2 class="abs sec-head" style="top:1776px"><i></i>OUR <span class="hl">CUSTOMERS</span></h2>
  <svg class="abs" style="left:125px;top:1847px" width="10" height="16" viewBox="0 0 10 16"><path d="M8 1 2 8l6 7" fill="none" stroke="#aaa" stroke-width="1.6"/></svg>
  <div class="abs logos">
    <span><i></i>Sonora</span>
    <span><i class="sq"></i>Northwind</span>
    <span>Pictavo</span>
    <span>Framestock</span>
    <span><i class="sq"></i>Quadrix</span>
    <span><i></i>Sonora</span>
  </div>
  <svg class="abs" style="left:1063px;top:1847px" width="10" height="16" viewBox="0 0 10 16"><path d="M2 1l6 7-6 7" fill="none" stroke="#aaa" stroke-width="1.6"/></svg>
</section>

<footer>
  <div class="abs footer"></div>
  <div class="abs brand foot-brand" style="left:160px;top:1950px"><span class="brand-mark"></span><span class="brand-name">Velorix Solutions</span></div>
  <p class="abs foot-about">Lorem Ipsum is simply dummy text of the printing and typesetting ind ustry. Lorem Ipsum has been the industry's standard dumm.</p>

  <div class="abs fcol" style="left:396px"><h4>QUICK LINKS</h4><ul><li>Home</li><li>Services</li><li>About us</li><li>Contact us</li><li>Join us</li><li>Partners.</li></ul></div>
  <div class="abs fcol" style="left:536px"><h4>RESOURCES</h4><ul><li>Demos</li><li>Documentation</li><li>Release History</li><li>Forums</li><li>Blogs</li><li>Developer Network</li></ul></div>
  <div class="abs fcol" style="left:709px"><h4>RECOGNITION</h4><ul><li>Key Customers</li><li>Success Stories</li><li>Testimonials</li><li>Awards</li></ul></div>
  <div class="abs fcol where" style="left:869px"><h4>WHERE TO FIND US</h4>
    <p><svg width="10" height="14" viewBox="0 0 10 14"><path d="M5 0a5 5 0 0 1 5 5c0 4-5 9-5 9S0 9 0 5a5 5 0 0 1 5-5z" fill="var(--red)"/><circle cx="5" cy="5" r="2" fill="#2a2a2a"/></svg><span>Harbour Lane 14, Block C<br>Ground Floor, Riverside<br>Zone-1180</span></p>
    <p class="tel"><svg width="12" height="12" viewBox="0 0 10 10"><path d="M2 0h3l1 3-1.5 1a6 6 0 0 0 2 2L7.5 4.5 10 5.5V8a2 2 0 0 1-2 2A8 8 0 0 1 0 2 2 2 0 0 1 2 0z" fill="var(--red)"/></svg>+420 555 010 733</p>
    <p><svg width="12" height="9" viewBox="0 0 12 9"><rect width="12" height="9" fill="var(--red)"/><path d="M0 0l6 5 6-5" fill="none" stroke="#2a2a2a"/></svg>info@velorix.example</p>
  </div>

  <div class="abs bottom">
    <span class="abs copy">Copyright 2016 &nbsp;All Rights Reserved.Velorix Solutions</span>
    <div class="abs socials"><span></span><span></span><span></span><span></span></div>
    <span class="abs code">C4</span>
  </div>
</footer>

</body>
</html>
```